label bath salt on glass bottle

for our bath salts (Flavours Rose, Lavender, Lemongras, mountain herbs, Mint, Cashmere) we need a label in the size of 50mm height an 55mm wide.

Target Market(s)

Prestige stores

Font styles to use
Serif
Script

Colors

Designer to choose colors to be used in the design.

Requirements
Must have
• Name of the label:
• Headline: Badesalz (can be also written in two words) Bade Salz
• Describtion of the sel: Totes Meer (comes from Dead Sea)
• Name of the different fragrances:
• Rose
• Pfingstrose (Peony)
• Lemongras
• Alpenkräuter (mountain herbs)
• Minze (mint)
• Cashmere
• Lavendel (lavender)
Nice to have
• Made with love in Switzerland
• Logos:
• Use our LOGO in the attachment or just
• PENIVO
• Switzerland

```html
<!DOCTYPE html>
<html lang="en">
<head>
<meta charset="utf-8">
<title>Bath Salt Lavender Label</title>
<link href="https://fonts.googleapis.com/css2?family=Yellowtail&family=Lato:wght@400&display=block" rel="stylesheet">
<style>
  :root {
    --backdrop-light: #f4f4f4;
    --backdrop-dark: #c9c9c9;
    --kraft: #c69a6d;
    --kraft-light: #d2a97d;
    --ink-brown: #6e4a2b;
    --ink-title: #6b4322;
  }
  html, body {
    margin: 0;
    padding: 0;
    width: 1200px;
    height: 900px;
    overflow: hidden;
  }
  body {
    background: radial-gradient(ellipse at center, var(--backdrop-light) 0%, var(--backdrop-dark) 100%);
    display: flex;
    align-items: center;
    justify-content: center;
  }
  .label {
    position: relative;
    width: 720px;
    height: 512px;
    background: linear-gradient(135deg, var(--kraft-light), var(--kraft));
    box-shadow: 0 10px 24px rgba(0,0,0,0.18);
  }
  .label-frame {
    position: absolute;
    inset: 0;
    width: 100%;
    height: 100%;
  }
  .label-title {
    position: absolute;
    top: 88px;
    left: 0;
    right: 0;
    margin: 0;
    text-align: center;
    font-family: "Yellowtail", "Brush Script MT", cursive;
    font-weight: 400;
    font-size: 104px;
    line-height: 1.1;
    color: var(--ink-title);
  }
  .label-fragrance {
    position: absolute;
    top: 232px;
    left: 0;
    right: 0;
    margin: 0;
    text-align: center;
    font-family: "Lato", sans-serif;
    font-size: 34px;
    line-height: 1;
    letter-spacing: 0.42em;
    padding-left: 0.42em;
    color: var(--ink-brown);
  }
  .label-sprig {
    position: absolute;
    top: 290px;
    left: 170px;
    width: 360px;
    height: 128px;
    border-radius: 64px 36px 36px 64px;
    background: linear-gradient(100deg, rgba(125,154,78,0.55) 0%, rgba(125,154,78,0.45) 50%, rgba(154,98,168,0.6) 100%);
  }
  .label-origin {
    position: absolute;
    top: 432px;
    left: 0;
    right: 0;
    margin: 0;
    text-align: center;
    font-family: "Lato", sans-serif;
    font-size: 16px;
    line-height: 1;
    letter-spacing: 0.3em;
    padding-left: 0.3em;
    color: var(--ink-brown);
  }
</style>
</head>
<body>
  <div class="label">
    <svg class="label-frame" viewBox="0 0 720 512" aria-hidden="true">
      <rect x="34" y="34" width="652" height="444" fill="none" stroke="var(--ink-brown)" stroke-width="2.5"/>
    </svg>
    <h1 class="label-title">Bath Salt</h1>
    <p class="label-fragrance">LAVENDER</p>
    <div class="label-sprig" role="img" aria-label="Illustration of a lavender sprig with green leaves and purple blossoms"></div>
    <p class="label-origin">TOTES MEER</p>
  </div>
</body>
</html>
```